Mining Engineering Services

I would like a 1 page flyer promoting RVT Mining Pty Ltd engineering services using a UAV (Unmanned aerial vehicle). I want something simple yet captures the readers attention. I have a promo video that I would like to attach a hyper link to this brochure. I have four other brochures to make after the successful completion of this one.

Target Market(s)

Mining Industry

Requirements
Must have
• Details from the word doc attached.
• Contact detail to be included;
• Dean Whitlock
• Email - dean.whitlock@rvtmining-example.com
• Phone - 0418552913

```html
<!DOCTYPE html>
<html lang="en">
<head>
<meta charset="utf-8">
<title>RVT Mining – UAV Engineering Services</title>
<link href="https://fonts.googleapis.com/css2?family=Oswald:wght@500&family=Roboto:wght@400;500&display=swap" rel="stylesheet">
<style>
:root{
  --blue:#3a9fd6;
  --navy:#1f5fa8;
  --ink:#222;
  --white:#fff;
  --earth-dark:#4a3628;
  --earth:#7a5a42;
  --earth-light:#9c7a5c;
}
*{margin:0;padding:0;box-sizing:border-box}
html,body{width:746px;height:1200px;overflow:hidden;background:var(--white)}
.flyer{position:relative;width:746px;height:1200px;font-family:Roboto,Arial,sans-serif;color:var(--ink);overflow:hidden}
.hero{position:absolute;left:0;top:0;width:746px;height:460px}
.brand{position:absolute;left:22px;top:0;width:292px;height:232px;background:var(--white);
  clip-path:polygon(0 0,100% 0,100% 88%,0 100%);display:flex;flex-direction:column;align-items:center;justify-content:center;gap:14px}
.brand-dot{width:74px;height:74px;border-radius:50%;background:var(--navy)}
.brand-name{font-family:Roboto,Arial,sans-serif;font-weight:500;font-size:26px;letter-spacing:4px;color:var(--navy)}
.section-title{font-family:Oswald,"Arial Narrow",sans-serif;font-weight:500;color:var(--navy);font-size:21px;text-transform:uppercase;
  border-bottom:1px solid var(--navy);display:inline-block;padding-right:8px;line-height:1.25}
.bio{position:absolute;left:26px;top:470px;width:400px}
.bio p{margin-top:10px;font-size:12.6px;line-height:1.38}
.services{position:absolute;left:26px;top:682px;width:420px}
.services ul{list-style:none;margin-top:10px}
.services li{position:relative;padding-left:25px;font-size:13.4px;height:26.4px;line-height:26.4px}
.services li::before{content:"";position:absolute;left:3px;top:10px;width:7px;height:7px;border-radius:50%;background:var(--blue)}
.uav-panel{position:absolute;left:443px;top:452px;width:303px;height:475px;background:var(--blue);border-bottom-left-radius:28px;
  color:var(--white);text-align:right;padding:20px 28px 0 20px}
.uav-panel .intro{font-size:18px;line-height:1.05;padding-right:6px}
.uav-panel .system{font-family:Oswald,"Arial Narrow",sans-serif;font-weight:500;font-size:20px;text-transform:uppercase;
  border-bottom:1px solid var(--white);display:inline-block;margin-top:6px;padding-left:6px;line-height:1.3}
.uav-panel ul{list-style:none;margin-top:12px}
.uav-panel li{position:relative;font-size:12.6px;line-height:1.05;padding-right:16px;margin-bottom:18px}
.uav-panel li::after{content:"";position:absolute;right:0;top:3px;width:7px;height:7px;border-radius:50%;background:var(--white)}
.sensors{position:absolute;right:30px;top:937px;text-align:right}
.sensors h3{font-family:Roboto,Arial,sans-serif;font-weight:500;font-size:13px;color:var(--navy);text-transform:uppercase;margin-bottom:6px}
.sensors li{list-style:none;position:relative;font-size:11.6px;line-height:19px;padding-right:12px}
.sensors li::after{content:"";position:absolute;right:0;top:7px;width:5px;height:5px;border-radius:50%;background:var(--blue)}
.footer{position:absolute;left:0;top:1060px;width:746px;height:140px}
.contact{position:absolute;left:0;top:1108px;width:746px;text-align:center;color:var(--white);font-weight:500;font-size:22px;line-height:32px}
.contact svg{vertical-align:-3px;margin-right:6px}
</style>
</head>
<body>
<div class="flyer">
  <svg class="hero" viewBox="0 0 746 460" role="img" aria-label="Aerial photograph of a mine site with haul road, trucks, scrub and a fixed-wing survey drone">
    <defs>
      <linearGradient id="earth" x1="0" y1="0" x2="1" y2="1">
        <stop offset="0" stop-color="var(--earth-dark)"/>
        <stop offset=".5" stop-color="var(--earth)"/>
        <stop offset="1" stop-color="var(--earth-light)"/>
      </linearGradient>
    </defs>
    <rect width="746" height="460" fill="url(#earth)"/>
    <path d="M0 395 Q380 470 746 355 L746 460 L0 460 Z" fill="var(--white)"/>
    <path d="M0 405 Q380 482 746 365" fill="none" stroke="var(--navy)" stroke-width="5"/>
  </svg>

  <div class="brand">
    <span class="brand-dot"></span>
    <span class="brand-name">RVT MINING</span>
  </div>

  <section class="bio">
    <h2 class="section-title">Company Short Bio</h2>
    <p>RVT Mining Pty Ltd is a Mining Engineering consultancy company with over 15 year's experience in the Mining industry. RVT Mining Pty Ltd provides value adding mining engineering services with the utilisation of industry leading UAV (Unmanned Aerial Vehicle) technology. RVT Mining utilises multiple sensors in the UAV to provide custom solutions to your Mine site. Unlike other UAV survey providers, RVT Mining's engineering expertise can provide assistance from concept to reconciliation of your project.</p>
  </section>

  <section class="services">
    <h2 class="section-title">Services include but are not limited to</h2>
    <ul>
      <li>Mine operation design and scheduling</li>
      <li>Pit optimisation</li>
      <li>Rehabilitation design and planning</li>
      <li>Surface water drainage</li>
      <li>Open pit/stockpile volumes</li>
      <li>DEM (Digital Elevation Models)</li>
      <li>Reconciliation reporting</li>
      <li>Thermal imaging for volatile materials</li>
      <li>Pit wall inspections</li>
      <li>Geo referenced Ortho-mosaics</li>
      <li>Site rehabilitation inspections</li>
      <li>Multispectral imaging</li>
      <li>Surveying services</li>
    </ul>
  </section>

  <aside class="uav-panel">
    <p class="intro">UAV (Unmanned Aerial<br>Vehicle) information</p>
    <h2 class="system">SkyTrace S200 UAV System</h2>
    <ul>
      <li>1.8m wing span</li>
      <li>Fully transportable</li>
      <li>Operates under fully autonomous<br>or manual control</li>
      <li>Highly accurate navigation and<br>positioning systems</li>
      <li>Versatile and flexible operations</li>
      <li>Long flight time + 45min<br>(large surveys per flight)</li>
      <li>Able to operate low rain</li>
      <li>Able to operate in high wind</li>
      <li>Parachute recovery</li>
      <li>Assisted Launch</li>
      <li>Multiple Pod &amp; Sensor Capable</li>
    </ul>
  </aside>

  <section class="sensors">
    <h3>Sensors utilised</h3>
    <ul>
      <li>RGB 24 mega pixel camera (Digital Elevation Models)</li>
      <li>Infra-red camera (Thermal imaging)</li>
      <li>NDVI (Multispectral imaging)</li>
      <li>Magnetometer (Magnetic surveys)</li>
    </ul>
  </section>

  <svg class="footer" viewBox="0 0 746 140" aria-hidden="true">
    <path d="M0 34 Q373 -8 746 30" fill="none" stroke="var(--navy)" stroke-width="3"/>
    <path d="M0 44 Q373 4 746 40 L746 140 L0 140 Z" fill="var(--blue)"/>
  </svg>
  <div class="contact">
    <div><svg width="20" height="20" viewBox="0 0 20 20" aria-hidden="true"><circle cx="10" cy="10" r="8.5" fill="none" stroke="#fff" stroke-width="1.6"/><path d="M7 5.5 L8.6 7.8 L7.7 9 Q8.7 11.2 11 12.3 L12.2 11.4 L14.5 13 L13.4 14.5 Q9.5 14.5 6 9 Q5.6 6.5 7 5.5 Z" fill="#fff"/></svg>0418552913</div>
    <div>Email - dean.whitlock@rvtmining-example.com</div>
  </div>
</div>
</body>
</html>
```